Premium Lawn fertiliser packaging - Looking for long term designer

*Update at bottom
I need a carefully considered, bold and professional packaging design for my new premium lawn fertiliser product. This contest is for a detailed front of the stand-up pouch packaging and once I’ve chosen a winner, they’ll be asked to create the layout for the back that links to the front as well. I have a full range of additional products that will also need designs and so I'm looking for someone who can do a great job here and who we can work with long term.

The front should include our logo for Pemberly Turf Supply Direct and be titled “Bloom Vigor Max” "Professional Lawn Fertiliser". The spring fertiliser tag line is "Awaken your lawn: Lush Greening, Lasting Health".
Beneath it, it then needs to include some important usage information and the key benefits along with some suitable graphic.

Key information to include:

Apply March - June
Treats 35-50 m2
16-3-8
+2%MgO + 1% Fe + 2.9% CaO (this is the chemical makeup of the fertiliser and needs to be fairly prominent. If you look at other professional fertiliser packaging, you'll see how it needs to compare).

Key features:
Premium fertiliser, used by professionals
Advanced greening with micro-nutrient complex
Dual action Nitrogen: Instant green boost & continuous feed for 3 months
Child & pet safe

Our brand colours are purple and green. Purple = #592999, Green = 3cb64a / 81d742 / 4d9d44

I think these colours look great against a white background.

Please make sure you look at our website as well to get an idea of our brand: www.pemberlyturfsupply.co.uk

To help, I've attached images of competitors fertiliser packaging that I like the look of. I'm not looking for you to copy but just see what type of thing appeals to me, the standard I'm expecting and what I need to compete against....

In addition, I have also attached some potential images you may wish to try using in your design, although please feel free to use your own if you have something better. For the moment, the images are 'preview' images, but once I decide on a design and we agree on the correct image, I will download and send over a fully licensed version.

*** Update*** When submitting your design, can you submit it in 2 formats: The first as a fully printed custom stand-up pouch and the second as a full-size label stuck onto a standup pouch (whatever colour you think is right for your design - choose white if you are not sure). To explain, I've just discovered we won't be able to get full custom bags printed in time for the first run and so we will have to opt for the design to be printed on labels and fixed onto bags. I therefore need to choose a design that works in both formats as both a label on a standup pouch as well as a fully printed pouch. Many thanks.

Target Market(s)

Domestic home-owners

Industry/Entity Type

Lawn care. NOT AGRICULTURE OR FARMING

Font styles to use
Sans Serif

Requirements
Must have
• Presented in 2 formats - see update at bottom of description
Nice to have
• I quite like designs against a white background, although I’m open to other ideas as well.
Should not have
• Please do not include any people or faces in the design. The text should be solid in colour, so no graduated colour fill in the text or outline text. Please avoid over-busy or cluttered designs.

```html
<!DOCTYPE html>
<html lang="en">
<head>
<meta charset="utf-8">
<title>Bloom Vigor Max – Professional Lawn Fertiliser</title>
<link href="https://fonts.googleapis.com/css2?family=Poppins:ital,wght@0,400;0,500;0,600;0,700;0,800;0,900;1,700;1,800&display=swap" rel="stylesheet">
<style>
  :root{
    --purple:#592999;
    --purple-deep:#47207d;
    --purple-dark:#3a1868;
    --green:#3cb64a;
    --green-light:#81d742;
    --green-dark:#4d9d44;
    --gold:#c9a24a;
    --white:#ffffff;
    --ink:#2b2b2b;
    --stage:#f4f4f6;
  }
  *{box-sizing:border-box;margin:0;padding:0}
  html,body{width:1200px;height:840px;overflow:hidden;background:var(--stage)}
  body{font-family:"Poppins",Arial,sans-serif;position:relative}

  .pouch{
    position:absolute;left:380px;top:30px;width:440px;height:780px;
    background:var(--purple);border-radius:10px 10px 6px 6px;overflow:hidden;
  }
  .pouch__seal{position:absolute;left:0;top:0;width:100%;height:46px;background:var(--purple-deep);
    border-bottom:2px solid var(--purple-dark)}
  .pouch__zip{position:absolute;left:0;top:70px;width:100%;height:3px;background:var(--purple-deep)}

  .label{
    position:absolute;left:24px;top:150px;width:392px;height:480px;background:var(--white);overflow:hidden;
  }
  .brand{position:absolute;top:22px;width:100%;display:flex;align-items:center;justify-content:center;gap:8px}
  .brand__dot{width:14px;height:14px;border-radius:50%;background:var(--green)}
  .brand__name{font-weight:600;font-size:15px;color:var(--ink);letter-spacing:.3px}

  .title{position:absolute;top:56px;width:100%;text-align:center;color:var(--purple);font-weight:800;line-height:1}
  .title__line1{font-size:62px;letter-spacing:-1px}
  .title__line2{font-size:44px;letter-spacing:-.5px;margin-top:2px}
  .title__accent{color:var(--green);font-weight:500}

  .subtitle{position:absolute;top:170px;left:62px;width:268px;height:26px;background:var(--green);
    color:var(--white);font-weight:700;font-size:15px;text-align:center;line-height:26px;z-index:2}

  .scene{position:absolute;top:184px;left:0;width:100%;height:296px;
    background:linear-gradient(180deg,#dfe9e4 0%,#9fb89a 22%,#5f8a45 38%,#4f8a2a 55%,#3f7a1e 80%,#2f5f17 100%)}

  .safe{position:absolute;top:202px;right:14px;width:84px;text-align:center;z-index:3}
  .safe__icon{width:58px;height:58px;margin:0 auto;border-radius:50%;background:#efe9f7;border:3px solid var(--gold)}
  .safe__word{display:block;margin-top:2px;font-weight:800;font-size:22px;color:var(--white);line-height:1}
  .safe__for{display:inline-block;background:var(--purple);color:var(--white);font-weight:700;font-size:9px;padding:1px 6px;margin-top:2px}

  .tagline{position:absolute;top:350px;left:16px;width:220px;color:var(--white);font-style:italic;font-weight:800;
    font-size:17px;line-height:1.12;z-index:3}

  .info{position:absolute;top:340px;right:16px;width:138px;height:128px;background:var(--green-dark);
    clip-path:polygon(0 0,100% 0,100% 92%,50% 100%,0 92%);color:var(--white);text-align:center;z-index:3;
    border-top:3px solid var(--green-light)}
  .info__season{font-weight:700;font-size:11px;margin-top:6px}
  .info__treats{font-size:9px;font-weight:500;margin-top:4px}
  .info__area{font-weight:800;font-size:26px;line-height:1}
  .info__npk{margin:4px auto 0;width:112px;background:var(--green);border:1px solid var(--white);font-weight:700;font-size:16px;line-height:22px}
  .info__trace{font-size:8px;font-weight:600;margin-top:4px}

  .swoosh{position:absolute;left:0;top:572px;width:440px;height:70px;z-index:2}

  .features{position:absolute;left:24px;top:660px;width:392px;display:flex;gap:10px}
  .feature{flex:1;display:flex;gap:4px;color:var(--white);font-size:9px;line-height:1.2}
  .feature + .feature{border-left:1px solid rgba(255,255,255,.35);padding-left:8px}
  .feature__tick{flex:none;width:11px;height:11px;margin-top:1px}
  .feature__head{display:block;font-weight:800;font-size:10px;text-transform:uppercase}
  .feature__head em{font-style:normal;color:var(--green-light)}
</style>
</head>
<body>
  <div class="pouch">
    <div class="pouch__seal"></div>
    <div class="pouch__zip"></div>

    <div class="label">
      <div class="brand"><span class="brand__dot"></span><span class="brand__name">Pemberly Turf Supply Direct</span></div>
      <div class="title">
        <div class="title__line1">BLOOM</div>
        <div class="title__line2">VIGOR <span class="title__accent">MAX</span></div>
      </div>
      <div class="subtitle">Professional Lawn Fertiliser</div>
      <div class="scene" role="img" aria-label="Photograph of a lush green lawn in front of a house with trees"></div>

      <div class="safe">
        <div class="safe__icon" role="img" aria-label="Illustration of a child playing with a dog"></div>
        <span class="safe__word">SAFE</span>
        <span class="safe__for">PETS &amp; KIDS</span>
      </div>

      <p class="tagline">Awaken Your Lawn<br>Lush Greening,<br>Lasting Health</p>

      <div class="info">
        <div class="info__season">Apply March - June</div>
        <div class="info__treats">Treats</div>
        <div class="info__area">35-50m²</div>
        <div class="info__npk">16 - 03 - 08</div>
        <div class="info__trace">2% MgO + 1% Fe + 2.9% CaO</div>
      </div>
    </div>

    <svg class="swoosh" viewBox="0 0 440 70" aria-hidden="true">
      <path d="M24 58 Q220 10 416 58 L416 70 L24 70 Z" fill="var(--purple)"/>
      <path d="M24 58 Q220 10 416 58" fill="none" stroke="var(--gold)" stroke-width="3"/>
    </svg>

    <div class="features">
      <div class="feature">
        <svg class="feature__tick" viewBox="0 0 12 12"><path d="M1 6.5 L4.5 10 L11 2" fill="none" stroke="var(--green-light)" stroke-width="2"/></svg>
        <span><span class="feature__head">Premium Fertiliser</span>used by professionals</span>
      </div>
      <div class="feature">
        <svg class="feature__tick" viewBox="0 0 12 12"><path d="M1 6.5 L4.5 10 L11 2" fill="none" stroke="var(--green-light)" stroke-width="2"/></svg>
        <span><span class="feature__head">Advanced <em>Greening</em></span>with micro-nutrient complex</span>
      </div>
      <div class="feature">
        <svg class="feature__tick" viewBox="0 0 12 12"><path d="M1 6.5 L4.5 10 L11 2" fill="none" stroke="var(--green-light)" stroke-width="2"/></svg>
        <span><span class="feature__head">Dual Action Nitrogen</span>Instant green boost &amp; continuous feed for 3 months</span>
      </div>
    </div>
  </div>
</body>
</html>
```